Marrowfield Transport Company Business Card Design

We are a company that delivers natural saltwater (from the ocean) to aquarium companies, restaurants and home marine tanks. I would like a new business card to suit.

Must include Name, company name, abn, contact number and website as well as logo (see attached).

Looking for a design that stands out, has a clean but unique appearance.

Double and single sided entries welcome

• Logo

```html
<!DOCTYPE html>
<html lang="en">
<head>
<meta charset="utf-8">
<title>Marrowfield Transport Company – Business Card</title>
<link rel="stylesheet" href="https://fonts.googleapis.com/css2?family=Cinzel:wght@500&family=Arimo:wght@400;700&family=Tinos:wght@700&display=swap">
<style>
  :root {
    --backdrop: #e9e6e1;
    --card-edge: #aebcf0;
    --card-mid: #dfe6fb;
    --card-light: #ffffff;
    --ink: #141414;
    --ink-soft: #2a2a2a;
    --brand-blue: #1f5fe0;
    --ornament-a: #e07ad8;
    --ornament-b: #f3d3ef;
    --icon-bg: #2b2b2b;
  }
  * { box-sizing: border-box; margin: 0; padding: 0; }
  html, body { width: 1200px; height: 900px; overflow: hidden; }
  body { background: var(--backdrop); position: relative; }

  .card {
    position: absolute;
    border-radius: 14px;
    overflow: hidden;
    background:
      radial-gradient(ellipse 60% 70% at 62% 62%, var(--card-light) 0%, rgba(255,255,255,0) 70%),
      linear-gradient(135deg, var(--card-edge) 0%, var(--card-mid) 45%, var(--card-light) 62%, var(--card-edge) 100%);
    box-shadow: 0 6px 18px rgba(0,0,0,0.25);
  }
  .card--front { left: 45px; top: 26px; width: 705px; height: 443px; }
  .card--back  { left: 563px; top: 460px; width: 603px; height: 418px; }

  .ornament {
    position: absolute;
    border-radius: 40px;
    opacity: 0.75;
  }
  .card--front .ornament {
    left: 0; top: 0; width: 330px; height: 120px;
    background: radial-gradient(ellipse at 30% 30%, var(--ornament-a) 0%, var(--ornament-b) 55%, rgba(243,211,239,0) 80%);
  }
  .card--back .ornament {
    left: 309px; top: 290px; width: 290px; height: 120px;
    background: radial-gradient(ellipse at 70% 60%, var(--ornament-a) 0%, var(--ornament-b) 55%, rgba(243,211,239,0) 80%);
  }

  .brand-mark {
    position: absolute; left: 440px; top: 62px;
    display: flex; align-items: center; gap: 12px;
    font-family: "Arimo", Arial, sans-serif;
    font-weight: 700; font-size: 30px; color: var(--brand-blue);
  }
  .brand-mark__square { width: 26px; height: 26px; background: var(--brand-blue); }

  .company-name {
    position: absolute; left: 26px; top: 200px;
    font-family: "Cinzel", "Times New Roman", serif;
    font-weight: 500; font-size: 36px; letter-spacing: 1px;
    color: var(--ink);
  }
  .company-tagline {
    position: absolute; left: 56px; top: 250px;
    font-family: "Arimo", Arial, sans-serif;
    font-size: 19px; color: var(--ink);
  }
  .person-name {
    position: absolute; left: 38px; top: 308px;
    font-family: "Arimo", Arial, sans-serif;
    font-size: 40px; color: var(--ink);
  }
  .phone {
    position: absolute; left: 38px; top: 376px;
    display: flex; align-items: center; gap: 14px;
    font-family: "Arimo", Arial, sans-serif;
    font-size: 33px; color: var(--ink);
  }
  .phone__icon { width: 28px; height: 28px; }

  .contact-list {
    position: absolute; left: 16px; top: 74px;
    list-style: none;
    font-family: "Tinos", "Times New Roman", serif;
    font-weight: 700; font-size: 19px; line-height: 28px;
    color: var(--ink-soft);
  }
</style>
</head>
<body>
  <section class="card card--front" aria-label="Business card front">
    <div class="ornament" role="img" aria-label="Pink floral swirl ornament"></div>
    <div class="brand-mark">
      <span class="brand-mark__square"></span>
      <span>Marrowfield</span>
    </div>
    <h1 class="company-name">MARROWFIELD</h1>
    <p class="company-tagline">Transport Company</p>
    <p class="person-name">Owen Tarrant</p>
    <p class="phone">
      <svg class="phone__icon" viewBox="0 0 28 28" aria-hidden="true">
        <rect width="28" height="28" rx="4" fill="var(--icon-bg)"/>
        <path d="M8 6 l4 0 l1.5 5 l-2.5 1.5 a10 10 0 0 0 4.5 4.5 l1.5 -2.5 l5 1.5 l0 4 a2 2 0 0 1 -2 2 a16 16 0 0 1 -14 -14 a2 2 0 0 1 2 -2 z" fill="#ffffff"/>
      </svg>
      <span>040 555 0182</span>
    </p>
  </section>

  <section class="card card--back" aria-label="Business card back">
    <ul class="contact-list">
      <li>Web:www.marrowfieldtransport.com.au</li>
      <li>E-mail:info@marrowfieldtransport.com.au</li>
      <li>ABN:12 345 678 901</li>
    </ul>
    <div class="ornament" role="img" aria-label="Pink and grey floral swirl ornament"></div>
  </section>
</body>
</html>
```